KR business cards
Business cards for Consulting outfit
Project: KR business cards
KR business cards -
Creative Brief
Professional
No name
No address
info@vosk-lantern.example
vosk-lantern.example
Would like business cards for 8 different people. No address on the card
Logo + We define the standard

```html
<!DOCTYPE html>
<html lang="en">
<head>
<meta charset="utf-8">
<title>vosk-lantern business card</title>
<link rel="stylesheet" href="https://fonts.googleapis.com/css2?family=Tinos&family=Arimo&display=swap">
<style>
  :root {
    --page: #f6f8f7;
    --card-top: #1d0b0c;
    --card-bottom: #030202;
    --ink-light: #b9b4b3;
    --ink-muted: #7f7674;
    --ink-contact: #8c8584;
    --accent: #c4242b;
    --divider: #5a1518;
  }
  * { margin: 0; padding: 0; box-sizing: border-box; }
  html, body {
    width: 1200px; height: 849px; overflow: hidden;
    background: var(--page);
  }
  .card {
    position: absolute; left: 271px; top: 230px;
    width: 661px; height: 364px; border-radius: 28px;
    background: linear-gradient(180deg, var(--card-top) 0%, #0c0405 55%, var(--card-bottom) 100%);
    overflow: hidden;
  }
  .card__divider {
    position: absolute; left: 396px; top: 40px; width: 1px; height: 285px;
    background: linear-gradient(180deg, transparent, var(--divider) 30%, var(--divider) 75%, transparent);
  }
  .person { position: absolute; left: 55px; top: 58px; font-family: "Tinos", serif; }
  .person__name { font-size: 29px; color: var(--ink-light); font-weight: 400; line-height: 1; }
  .person__role { font-size: 16px; color: var(--ink-muted); margin-top: 2px; }
  .contacts { position: absolute; left: 64px; top: 180px; list-style: none; font-family: "Arimo", sans-serif; }
  .contacts__item {
    display: flex; align-items: center; height: 32px;
    font-size: 15px; color: var(--ink-contact);
  }
  .contacts__icon { width: 18px; height: 18px; margin-right: 14px; flex: none; }
  .brand {
    position: absolute; left: 396px; right: 0; top: 150px;
    display: flex; flex-direction: column; align-items: center;
  }
  .brand__mark { width: 26px; height: 26px; background: var(--accent); }
  .brand__name {
    margin-top: 12px; font-family: "Tinos", serif; font-size: 23px; color: var(--ink-muted);
  }
</style>
</head>
<body>
  <div class="card">
    <div class="person">
      <h1 class="person__name">Teodor Marsic</h1>
      <p class="person__role">Graphic designer</p>
    </div>
    <ul class="contacts">
      <li class="contacts__item">
        <svg class="contacts__icon" viewBox="0 0 18 18"><path d="M4 2h3l1.5 4-2 1.2a9 9 0 0 0 4.3 4.3L12 9.5l4 1.5v3a2 2 0 0 1-2 2A12 12 0 0 1 2 4a2 2 0 0 1 2-2z" fill="var(--accent)"/></svg>
        014 / 5521-640-27
      </li>
      <li class="contacts__item">
        <svg class="contacts__icon" viewBox="0 0 18 18"><rect x="2" y="3" width="14" height="10" rx="2" fill="var(--accent)"/><path d="M5 13v3l3-3z" fill="var(--accent)"/></svg>
        2417 / 3960-215-7724
      </li>
      <li class="contacts__item">
        <svg class="contacts__icon" viewBox="0 0 18 18"><rect x="2" y="4" width="14" height="10" rx="2" fill="none" stroke="var(--accent)" stroke-width="2"/><path d="M3 5l6 5 6-5" fill="none" stroke="var(--accent)" stroke-width="1.6"/></svg>
        info@vosk-lantern.example
      </li>
      <li class="contacts__item">
        <svg class="contacts__icon" viewBox="0 0 18 18"><circle cx="9" cy="9" r="7" fill="none" stroke="var(--accent)" stroke-width="2"/><path d="M2 9h14M9 2c-3 3.5-3 10.5 0 14M9 2c3 3.5 3 10.5 0 14" fill="none" stroke="var(--accent)" stroke-width="1.2"/></svg>
        vosk-lantern.example
      </li>
    </ul>
    <div class="card__divider"></div>
    <div class="brand">
      <span class="brand__mark"></span>
      <span class="brand__name">vosk-lantern</span>
    </div>
  </div>
</body>
</html>
```